Bref créative
Vantoria Real Estate
A Forward Thinking Real Estate Company
Modern
Luke Tarrel
President
4817 North Bramwick Road
Atlanta, Georgia 61837
Luke@Vantoria.com
www.vantoria.com
Please keep in mind that the business card will be printed with rounded edges on the corners (they will not be pointed edges).
As for the font, I use two different fonts in the logo - HandelGotDBol and Arial. I think we should use Ariel font for the text of the business card.
Finally, I am looking for a business card design that is unique and out of the box. Looking for creativity and truly something unique with a nice combination of the reds and blacks used in the logo. I have uploaded the AI file for the logo.
The back of the business card must contain the logo and slogan.
In addition, the following descriptive words must be included somewhere in a unique format:
Brokerage -
Consulting -
Development -
Investments -
Management
And finally, the back of the business card must also contain the website address of the company -
this is the AI file with the company logo
front of card with new bottom

```html
<!DOCTYPE html>
<html lang="en">
<head>
<meta charset="utf-8">
<title>Vantoria Real Estate — Business Cards</title>
<link href="https://fonts.googleapis.com/css2?family=Arimo:wght@400;700&display=swap" rel="stylesheet">
<style>
  :root {
    --bg: #d9dadc;
    --card-white: #ffffff;
    --card-white-shade: #e9e9ea;
    --ink: #2b2b2b;
    --ink-soft: #5c5c5c;
    --brand-red: #c8161d;
    --brand-red-dark: #8f0c11;
    --black-top: #3a3a3a;
    --black-bottom: #111111;
    --light-text: #e8e8e8;
    --dim-text: #9a9a9a;
  }
  * { box-sizing: border-box; margin: 0; padding: 0; }
  html, body {
    width: 1200px; height: 891px; overflow: hidden;
    background: var(--bg);
    font-family: "Arimo", Arial, sans-serif;
  }
  .sheet {
    position: relative; width: 1200px; height: 891px;
  }
  .card {
    position: absolute;
    width: 520px; height: 297px;
    border-radius: 18px;
    overflow: hidden;
    box-shadow: 0 6px 18px rgba(0,0,0,0.18);
  }
  .card--front-a { left: 60px; top: 120px; }
  .card--back-black { left: 620px; top: 120px; }
  .card--front-b { left: 60px; top: 474px; }
  .card--back-red { left: 620px; top: 474px; }

  /* Front */
  .front {
    background: linear-gradient(180deg, var(--card-white) 55%, var(--card-white-shade) 100%);
    color: var(--ink);
  }
  .brand {
    position: absolute; left: 34px; top: 46px;
  }
  .brand__row { display: flex; align-items: center; gap: 10px; }
  .brand__mark {
    width: 34px; height: 34px; border-radius: 4px;
    background: var(--brand-red);
  }
  .brand__name {
    font-weight: 700; font-size: 40px; letter-spacing: 0.5px;
    color: var(--ink); line-height: 1;
  }
  .brand__tagline {
    margin-top: 6px; font-size: 10.5px; color: var(--brand-red);
  }
  .person {
    position: absolute; left: 300px; top: 108px;
  }
  .person__name { font-weight: 700; font-size: 17px; color: var(--ink); }
  .person__title { font-size: 10px; color: var(--ink-soft); margin-top: 3px; }
  .card--front-b .person__name { color: var(--brand-red); }

  .contact {
    position: absolute; left: 34px; top: 182px;
    font-size: 10px; line-height: 1.45; color: var(--ink-soft);
  }
  .contact__label { font-weight: 700; color: var(--ink); }
  .contact__web { color: var(--ink); }
  .contact__web strong { color: var(--brand-red); }

  .front-tab {
    position: absolute; left: 0; top: 206px; width: 10px; height: 40px;
    background: #bdbdbd;
  }
  .front-band {
    position: absolute; left: 0; bottom: 0; width: 100%; height: 14px;
    background: linear-gradient(90deg, var(--brand-red) 0 6%, var(--card-white-shade) 6% 100%);
  }

  /* Back */
  .back { color: var(--light-text); }
  .back--black { background: linear-gradient(180deg, var(--black-top), var(--black-bottom)); }
  .back--red { background: linear-gradient(180deg, var(--brand-red), var(--brand-red-dark)); }
  .back__brand {
    position: absolute; left: 0; right: 0; top: 62px;
    display: flex; justify-content: center; align-items: center; gap: 10px;
  }
  .back__mark { width: 30px; height: 30px; border-radius: 4px; background: var(--brand-red); }
  .back--red .back__mark { background: var(--light-text); }
  .back__name { font-weight: 700; font-size: 30px; color: var(--light-text); letter-spacing: 0.5px; }
  .services {
    position: absolute; left: 0; right: 0; top: 128px;
    text-align: center; font-size: 12px; line-height: 1.6; color: var(--light-text);
  }
  .services span { margin: 0 8px; }
  .services span::before { content: "\2022"; margin-right: 5px; color: var(--dim-text); }
  .back--red .services span::before { color: #f1b3b5; }
  .back__web {
    position: absolute; left: 0; right: 0; bottom: 44px;
    text-align: center; font-size: 12px; letter-spacing: 4px; color: var(--dim-text);
  }
  .back--red .back__web { color: #f4c3c5; }
</style>
</head>
<body>
<main class="sheet">

  <section class="card card--front-a front" aria-label="Card front, white">
    <div class="brand">
      <div class="brand__row"><span class="brand__mark"></span><span class="brand__name">VANTORIA</span></div>
      <p class="brand__tagline">A Forward Thinking Real Estate Company</p>
    </div>
    <div class="person">
      <p class="person__name">Luke Tarrel</p>
      <p class="person__title">President</p>
    </div>
    <div class="contact">
      <p>4817 North Bramwick Road</p>
      <p>Atlanta, Georgia 61837</p>
      <p><span class="contact__label">P:</span> (404) 555-0137 <span class="contact__label">F:</span> (404) 555-0182</p>
      <p><span class="contact__label">E:</span> Luke@Vantoria.com</p>
      <p class="contact__web">www.<strong>vantoria</strong>.com</p>
    </div>
    <span class="front-tab"></span>
  </section>

  <section class="card card--back-black back back--black" aria-label="Card back, black">
    <div class="back__brand"><span class="back__mark"></span><span class="back__name">VANTORIA</span></div>
    <p class="services">
      <span>Brokerage</span><span>Consulting</span><span>Development</span><br>
      <span>Investments</span><span>Management</span>
    </p>
    <p class="back__web">www.vantoria.com</p>
  </section>

  <section class="card card--front-b front" aria-label="Card front, white with red edge">
    <div class="brand">
      <div class="brand__row"><span class="brand__mark"></span><span class="brand__name">VANTORIA</span></div>
      <p class="brand__tagline">A Forward Thinking Real Estate Company</p>
    </div>
    <div class="person">
      <p class="person__name">Luke Tarrel</p>
      <p class="person__title">President</p>
    </div>
    <div class="contact">
      <p>4817 North Bramwick Road</p>
      <p>Atlanta, Georgia 61837</p>
      <p><span class="contact__label">P:</span> (404) 555-0137 <span class="contact__label">F:</span> (404) 555-0182</p>
      <p><span class="contact__label">E:</span> Luke@Vantoria.com</p>
      <p class="contact__web">www.<strong>vantoria</strong>.com</p>
    </div>
    <span class="front-band"></span>
  </section>

  <section class="card card--back-red back back--red" aria-label="Card back, red">
    <div class="back__brand"><span class="back__mark"></span><span class="back__name">VANTORIA</span></div>
    <p class="services">
      <span>Brokerage</span><span>Consulting</span><span>Development</span><br>
      <span>Investments</span><span>Management</span>
    </p>
    <p class="back__web">www.vantoria.com</p>
  </section>

</main>
</body>
</html>
```